Surgical Conditions of the thyroid and parathyroid glands - a flyer for GPs

Hi there,

I am a thyroid surgeon trying to produce a bi-fold A4 flyer as a quick reference guide for general practitioners (family doctors). It needs to feel friendly and professional.

The text for the four "pages" can be found in the "thyroid flyer for design" document attached.

The front page should have:
- The title
- the photo with the patient having an ultrasound
- the photo of the asian woman with the enlarged thyroid gland
- possibly the photo of the blonde woman touching her neck

The inner two pages are predominantly text - I would love this to be presented in an easy to read, uncluttered format. There is a photo attached which demonstrates the parathyroid glands. This should be placed near the parathyroid text section if possible.

The back page is a brief bio of myself. It should have the profile pic attached.
It should have contact details, which I forgot to put in the word document. These details are:
Phone (03) 9418 2759 for all appointments
Consulting at:
27 Pellory Lane, Harwood Vale, VIC 3999
norvalesurgical.example.au
tobinmarwick.example

The back page should also have the "Tarrow Health" and "Guild of Operatives" logos.

If possible, all pages should have the "Norvale Surgical Group" logo.

The whole feel could have a similar colour scheme to my group website (largely orange and green). Please see www.norvalesurgical.example.au for examples.

Many thanks!

Target Market(s)

General practitioners (ie family doctors)

Industry/Entity Type

Medical And Science

Font styles to use
Sans Serif

Colors
33b8a4
f78f20

Requirements
Must have
• Contact details on the back, norvale surgical group logo on front and back pages, Tarrow Health and Guild of Operatives logo on the back.
Nice to have
• Other medical/surgical related images as you see fit - sorry to be so broad!!

```html
<!DOCTYPE html>
<html lang="en">
<head>
<meta charset="utf-8">
<title>Surgical Conditions of the Thyroid and Parathyroid Glands – Norvale Surgical Group</title>
<link rel="stylesheet" href="https://fonts.googleapis.com/css2?family=Open+Sans:wght@300;400;600;700&display=swap">
<style>
  :root{
    --orange:#d9882f;
    --orange-bright:#f78f20;
    --teal:#33b8a4;
    --teal-soft:#7cc7b8;
    --white:#ffffff;
    --paper:#f4f4f6;
    --ink:#3a3a3a;
    --backdrop:#8f8f8f;
    --photo-a:#c9c5cf;
    --photo-b:#e2cfc4;
    --partner-blue:#2f5fa8;
  }
  *{box-sizing:border-box;margin:0;padding:0}
  html,body{width:1200px;height:789px;overflow:hidden}
  body{background:var(--backdrop);font-family:"Open Sans",Arial,sans-serif;position:relative}
  .spread{position:absolute;left:105px;top:44px;width:990px;height:700px;display:flex;box-shadow:0 6px 18px rgba(0,0,0,.25)}
  .page{position:relative;width:495px;height:700px;overflow:hidden}
  .page-art{position:absolute;inset:0;width:100%;height:100%}

  /* back page */
  .back-page{background:var(--orange);color:var(--white)}
  .portrait{position:absolute;left:28px;top:60px;width:152px;height:110px;border:4px solid var(--white);background:linear-gradient(135deg,#dfe3e6,#8d949c 60%,#b9bec4)}
  .about-title{position:absolute;left:192px;top:52px;font-size:20px;font-weight:400;padding-bottom:2px;border-bottom:1px solid var(--white);width:150px}
  .about-lead{position:absolute;left:192px;top:86px;width:240px;font-size:8.6px;line-height:1.38}
  .about-body{position:absolute;left:28px;top:180px;width:420px;font-size:8.6px;line-height:1.38}
  .about-body p{margin-bottom:7px}
  .conditions{position:absolute;font-size:9px;line-height:1.45}
  .conditions h3{font-size:10.5px;font-weight:700;margin-bottom:3px}
  .conditions ul{list-style:none}
  .conditions li{position:relative;padding-left:13px}
  .conditions li::before{content:"";position:absolute;left:1px;top:3px;width:6px;height:3px;border-left:1.5px solid var(--white);border-bottom:1.5px solid var(--white);transform:rotate(-45deg)}
  .conditions-general{left:28px;top:412px;width:200px}
  .conditions-endocrine{left:252px;top:372px;width:210px}
  .contact{position:absolute;left:28px;top:578px;width:300px}
  .contact-call{font-size:13px;font-weight:600;display:flex;align-items:center;gap:5px}
  .contact-call .phone-number{font-size:11px;font-weight:700}
  .contact-heading{font-size:15px;font-weight:700;line-height:1.1}
  .contact-consult{font-size:14px;font-weight:400;margin:2px 0 6px}
  .contact-list{list-style:none;font-size:10.5px;line-height:1.5}
  .contact-list li{display:flex;align-items:center;gap:6px;white-space:nowrap}
  .contact-list svg{width:10px;height:10px;flex:none}
  .partner-badges{position:absolute;left:372px;top:600px;width:123px;height:100px}
  .badge-plain{position:absolute;left:16px;top:10px;width:32px;height:32px;border-radius:6px;background:var(--orange)}
  .partner-name{position:absolute;left:6px;top:56px;font-size:14px;font-weight:600;color:var(--partner-blue);white-space:nowrap}

  /* front page */
  .front-page{background:var(--paper);color:var(--white)}
  .neck-photo{position:absolute;left:0;top:0;width:495px;height:300px}
  .title-block{position:absolute;left:215px;top:300px;width:265px}
  .title-kicker{font-size:14px;font-weight:400;letter-spacing:.3px}
  .title-main{font-size:18px;font-weight:700;line-height:1.08;text-transform:uppercase}
  .title-sub{font-size:12.5px;font-weight:400;margin-top:4px;text-transform:uppercase;line-height:1.2}
  .group-name{position:absolute;left:170px;top:572px;display:flex;align-items:center;gap:10px;color:var(--ink)}
  .group-mark{width:22px;height:22px;border-radius:50%;background:var(--teal);flex:none}
  .group-name .name-main{font-size:26px;font-weight:700;letter-spacing:1px;line-height:1}
  .group-name .name-sub{font-size:10px;font-weight:400;letter-spacing:1.5px}
  .front-web{position:absolute;right:18px;top:648px;font-size:10.5px;color:var(--ink)}
  .front-web span{color:var(--orange-bright);font-weight:600}
</style>
</head>
<body>
<main class="spread">

  <section class="page back-page">
    <svg class="page-art" viewBox="0 0 495 700" aria-hidden="true">
      <path d="M372 0 C410 120 455 200 495 240 L495 0 Z" fill="#e6e6ea"/>
      <path d="M408 0 C440 90 470 150 495 180 L495 0 Z" fill="#cfc6c8"/>
      <circle cx="495" cy="655" r="150" fill="var(--teal)"/>
      <circle cx="495" cy="660" r="126" fill="var(--white)"/>
      <path d="M372 700 C380 640 410 580 455 545" stroke="#c9cbd0" stroke-width="10" fill="none"/>
    </svg>

    <div class="portrait" role="img" aria-label="Portrait of the surgeon in a grey suit seated at his desk"></div>
    <h2 class="about-title">About Tobin</h2>
    <p class="about-lead">Tobin is a graduate of Tarrow University (Bachelor of Medicine, Bachelor of Surgery, 2000) and has been a fellow of the Royal Australasian Guild of Operatives since 2009.</p>
    <div class="about-body">
      <p>Tobin's surgical interests include benign and malignant disease of the thyroid and parathyroid glands, endoscopic trans-axillary and trans-oral thyroid surgery, and management of adrenal disease. He is the head of paediatric endocrine surgery at Tarrow Children's Hospital. He is happy to perform ultrasound-guided fine needle aspirates for most thyroid nodules as required, at an advantage to patients in terms of time and cost.</p>
      <p>Away from medicine, Tobin is a classically-trained flautist and jazz saxophonist who plays with the Southern Physicians Orchestra. He is a keen follower of the Kelvale football club and the Tallis cricket club. Tobin travels overseas regularly with projectHARBOR, a charity currently building a trauma centre on the east coast, a region affected by the Boxing Day tsunami and civil war.</p>
      <p>Tobin has public appointments with Tarrow Health (Ashcombe, Merrin, Harwood Vale and Lindell), Eastmere Health and St Aldric's. He is an accredited specialist surgeon at The Glade, The Crescent, Ashworth Kelso and St Brennan Private Hospitals.</p>
    </div>

    <div class="conditions conditions-general">
      <h3>General surgical conditions:</h3>
      <ul>
        <li>Laparoscopic cholecystectomy</li>
        <li>Abdominal hernias (inguinal, umbilical, incisional)</li>
        <li>Lipomas</li>
        <li>Skin lesions</li>
        <li>Carpal tunnel release</li>
        <li>Ingrown toenails</li>
        <li>Vasectomy</li>
      </ul>
    </div>
    <div class="conditions conditions-endocrine">
      <h3>Endocrine conditions:</h3>
      <ul>
        <li>Thyroid nodules</li>
        <li>Thyroid cancer</li>
        <li>Graves' disease/thyrotoxicosis</li>
        <li>Multinodular goitre</li>
        <li>Parathyroid disease</li>
        <li>Adrenal disease</li>
      </ul>
    </div>

    <div class="contact">
      <p class="contact-call">Call
        <svg width="12" height="12" viewBox="0 0 24 24" aria-hidden="true"><path fill="#fff" d="M6.6 10.8a15.1 15.1 0 0 0 6.6 6.6l2.2-2.2c.3-.3.7-.4 1-.2 1.1.4 2.3.6 3.6.6.6 0 1 .4 1 1V20c0 .6-.4 1-1 1A17 17 0 0 1 3 4c0-.6.4-1 1-1h3.5c.6 0 1 .4 1 1 0 1.2.2 2.4.6 3.6.1.3 0 .7-.2 1z"/></svg>
        <span class="phone-number">(03) 9418 2759</span></p>
      <p class="contact-heading">For All Appointments</p>
      <p class="contact-consult">Consulting at:</p>
      <ul class="contact-list">
        <li><svg viewBox="0 0 24 24" aria-hidden="true"><path fill="#fff" d="M12 2a7 7 0 0 0-7 7c0 5 7 13 7 13s7-8 7-13a7 7 0 0 0-7-7zm0 9.5a2.5 2.5 0 1 1 0-5 2.5 2.5 0 0 1 0 5z"/></svg>27 Pellory Lane, Harwood Vale, VIC 3999</li>
        <li><svg viewBox="0 0 24 24" aria-hidden="true"><circle cx="12" cy="12" r="10" fill="none" stroke="#fff" stroke-width="2.4"/><path d="M2 12h20M12 2c3 3 3 17 0 20M12 2c-3 3-3 17 0 20" stroke="#fff" stroke-width="2" fill="none"/></svg>norvalesurgical.example.au</li>
        <li><svg viewBox="0 0 24 24" aria-hidden="true"><circle cx="12" cy="12" r="10" fill="none" stroke="#fff" stroke-width="2.4"/><path d="M2 12h20M12 2c3 3 3 17 0 20M12 2c-3 3-3 17 0 20" stroke="#fff" stroke-width="2" fill="none"/></svg>tobinmarwick.example</li>
      </ul>
    </div>

    <div class="partner-badges">
      <div class="badge-plain" role="img" aria-label="Guild of Operatives fellowship badge"></div>
      <p class="partner-name">Tarrow Health</p>
    </div>
  </section>

  <section class="page front-page">
    <svg class="page-art" viewBox="0 0 495 700" aria-hidden="true">
      <defs>
        <linearGradient id="neckTone" x1="0" y1="0" x2="1" y2="1">
          <stop offset="0" stop-color="#b9a89a"/>
          <stop offset=".45" stop-color="var(--photo-b)"/>
          <stop offset="1" stop-color="var(--photo-a)"/>
        </linearGradient>
        <radialGradient id="goitreTone" cx=".5" cy=".45" r=".6">
          <stop offset="0" stop-color="#c9a98a"/>
          <stop offset="1" stop-color="#8c6a50"/>
        </radialGradient>
        <linearGradient id="scanTone" x1="0" y1="0" x2="1" y2="1">
          <stop offset="0" stop-color="#e8e8ec"/>
          <stop offset="1" stop-color="#8f8688"/>
        </linearGradient>
      </defs>
      <rect width="495" height="460" fill="url(#neckTone)"/>
      <path d="M0 0 L38 0 C28 110 40 210 75 290 L0 290 Z" fill="#e6e6ea"/>
      <path d="M0 700 L0 430 C140 360 330 300 495 235 L495 700 Z" fill="var(--orange)"/>
      <path d="M0 700 L0 430 C140 360 330 300 495 235 L495 258 C330 325 170 415 95 545 C72 590 62 645 60 700 Z" fill="var(--teal)"/>
      <path d="M0 700 L0 520 C25 505 45 470 60 440 C40 520 40 620 44 700 Z" fill="var(--teal-soft)" opacity=".6"/>
      <path d="M80 700 C90 560 200 480 495 432 L495 700 Z" fill="var(--white)"/>
      <path d="M68 700 C78 555 190 470 495 420" stroke="#e4e4ea" stroke-width="6" fill="none"/>
      <circle cx="40" cy="345" r="74" fill="var(--teal-soft)"/>
      <circle cx="40" cy="345" r="64" fill="url(#goitreTone)"/>
      <circle cx="420" cy="462" r="58" fill="var(--white)"/>
      <circle cx="420" cy="462" r="52" fill="url(#scanTone)"/>
    </svg>
    <div class="neck-photo" role="img" aria-label="Photo of a woman touching her neck, shown from the jaw to the collarbone"></div>
    <div class="goitre-photo" role="img" aria-label="Photo of a patient's neck showing an enlarged thyroid gland"></div>
    <div class="scan-photo" role="img" aria-label="Photo of a patient lying back during a neck ultrasound"></div>

    <div class="title-block">
      <p class="title-kicker">SURGICAL CONDITIONS</p>
      <h1 class="title-main">Of the thyroid<br>and parathyroid<br>glands</h1>
      <p class="title-sub">A quick reference guide<br>for GPs</p>
    </div>

    <div class="group-name">
      <span class="group-mark"></span>
      <div>
        <p class="name-main">NORVALE</p>
        <p class="name-sub">SURGICAL GROUP</p>
      </div>
    </div>
    <p class="front-web">www.<span>norvalesurgical</span>.example.au</p>
  </section>

</main>
</body>
</html>
```